Flyer design for mental health and disability support work company.

The company name 'Marlow Disability'

we need a flyer design for our company.

Specialising
Marlow Disability is a new RFTQ service aimed towards RFTQ participants with psychosocial/mental health, intellectual, and cognitive disabilities. We also specialise in supporting participants with a history of being involved in the criminal justice system.

Our focus
Focusing on providing core RFTQ supports for community participation, daily activities and supported independent living.

Authentic
Like-minded people passionate about wanting to make a difference in participants' lives.

Our aim is to provide holistic and empowering support targeted towards creating independence and guidance for all participants and families.

Over 35 years of experience working with people with a vast range of disabilities and individual support needs.

Extensive experience not only within RFTQ but working with mainstream services within Ulmera Justice, Health, Corrections and Parole, Housing, Keystep Hub, Paywarden, Lawbridge, PMTQ and NSW court systems.

website www.marlowdisability.com.au
email for referrals send to - referrals@marlowdisability.com.au
for further information send to - hello@marlowdisability.com.au

number 1800 372 519

Font styles to use
Serif

Requirements
Should not have
• pictures with people that have disabilities

```html
<!DOCTYPE html>
<html lang="en">
<head>
<meta charset="utf-8">
<title>Marlow Disability Flyer</title>
<link href="https://fonts.googleapis.com/css2?family=Roboto:wght@400;500;700;900&family=Oswald:wght@500;600&family=Yellowtail&display=swap" rel="stylesheet">
<style>
  :root{
    --navy:#03226b;
    --band:#0f4699;
    --gold:#dba90a;
    --sky:#80c8f7;
    --ink:#1b1b1b;
    --white:#ffffff;
    --stage:#dde3e2;
  }
  *{margin:0;padding:0;box-sizing:border-box}
  html,body{width:1200px;height:1200px;overflow:hidden;background:var(--stage)}
  body{position:relative;font-family:'Roboto',sans-serif}
  .flyer{position:absolute;left:175px;top:50px;width:1164px;height:1506px;background:var(--white);
    transform:scale(0.7304);transform-origin:0 0;overflow:hidden;box-shadow:8px 10px 18px rgba(0,0,0,.35)}
  .abs{position:absolute}
  .brand{left:40px;top:37px;display:flex;align-items:center;gap:16px}
  .brand-mark{width:150px;height:150px;border-radius:50%;background:var(--navy)}
  .brand-name{font-weight:700;font-size:24px;color:var(--navy);line-height:1.2;width:130px}
  .tagline{left:37px;top:220px;font-size:26px;letter-spacing:9.4px;color:var(--ink);font-weight:400}
  .lead{left:37px;top:286px;font-size:39px;color:var(--ink);font-weight:400}
  .headline{left:34px;font-size:64px;font-weight:900;line-height:1;letter-spacing:-0.5px}
  .headline.navy{top:330px;color:var(--navy)}
  .headline.gold{top:393px;color:var(--gold)}
  .script{left:36px;top:440px;font-family:'Yellowtail','Brush Script MT',cursive;font-size:118px;color:var(--sky);line-height:1;z-index:3;
    -webkit-text-stroke:3px var(--white);paint-order:stroke fill}
  .photo{left:570px;top:0;width:594px;height:539px;
    background:linear-gradient(120deg,#c9d2d3 0%,#e9eef0 35%,#f5f3f1 55%,#d8dde0 70%,#c9542e 88%,#e2602f 100%)}
  .panel-navy{left:0;top:539px;width:570px;height:885px;background:var(--navy)}
  .band{left:0;top:945px;width:570px;height:236px;background:var(--band)}
  .sec-title{font-size:29px;font-weight:500;color:var(--gold);line-height:1}
  .sec-text{font-size:17px;color:var(--white);line-height:29px;width:500px}
  .over{left:37px;top:966px;font-size:41px;font-weight:500;color:var(--white);line-height:1}
  .years{left:37px;top:1008px;font-family:'Oswald',sans-serif;font-weight:600;font-size:86px;line-height:1;color:var(--white);
    letter-spacing:-1px;white-space:nowrap;transform:scaleX(0.84);transform-origin:0 0}
  .years .num{color:var(--gold)}
  .experience{left:332px;top:1020px;font-size:35px;font-weight:700;color:var(--white);line-height:34px;white-space:nowrap}
  .experience .small{font-size:33px}
  .goldbar{left:38px;top:1103px;width:493px;height:43px;background:var(--gold);color:var(--navy);
    font-size:28px;font-weight:700;text-align:center;line-height:43px}
  .cond{display:flex;align-items:center;gap:18px;color:var(--white);font-size:20px;font-weight:500}
  .cond svg{flex:none}
  .aim-title{left:612px;top:611px;font-size:29px;color:var(--gold);font-weight:400;line-height:1}
  .aim-title b{font-weight:700}
  .aim-text{left:612px;top:651px;width:500px;font-size:17px;line-height:24.5px;color:var(--ink)}
  .exp-title{left:612px;top:792px;font-size:29px;line-height:33px;color:var(--navy);font-weight:500}
  .exp-title .hl{color:var(--gold);font-weight:700}
  .vdash{left:868px;top:886px;height:480px;border-left:2px dashed #b9bfcc}
  .hdash{height:0;border-top:2px dashed #c3c8d3;width:230px}
  .svc{display:flex;align-items:center;gap:14px;font-size:20px;color:var(--ink)}
  .svc svg{flex:none}
  .footer-gold{left:0;top:1424px;width:520px;height:82px;background:var(--gold)}
  .footer-sky{left:450px;top:1414px;width:714px;height:92px;background:var(--sky);border-top-left-radius:70px 60px;border-top:8px solid var(--white)}
  .phone{left:38px;top:1440px;display:flex;align-items:center;gap:20px;color:var(--white);font-size:48px;font-weight:700;line-height:50px}
  .contact{display:flex;align-items:center;gap:12px;color:var(--white);font-size:18px}
</style>
</head>
<body>
<div class="flyer">

  <div class="abs brand">
    <div class="brand-mark"></div>
    <div class="brand-name">Marlow Disability</div>
  </div>

  <div class="abs tagline">LIKEMINDED PEOPLE</div>
  <div class="abs lead">WANTING TO MAKE A</div>
  <div class="abs headline navy">DIFFERENCE IN</div>
  <div class="abs headline gold">PARTICIPANT'S</div>

  <div class="abs photo" role="img" aria-label="Photo of a support worker in a white coat holding a client's hands across a desk"></div>

  <div class="abs panel-navy"></div>
  <div class="abs band"></div>
  <div class="abs script">Lives</div>

  <div class="abs sec-title" style="left:37px;top:625px">SPECIALISING</div>
  <div class="abs sec-text" style="left:37px;top:664px">Marlow Disability is a new RFTQ service aimed toward RFTQ parti-cipants with a history of criminal justice, psychosocial/mental health, intellectual, and cognitive disabilities.</div>

  <div class="abs sec-title" style="left:37px;top:804px">OUR FOCUS</div>
  <div class="abs sec-text" style="left:37px;top:839px;line-height:32px">Focusing on providing core RFTQ supports for community partici-pation, daily activities and supported independent living.</div>

  <div class="abs over">OVER</div>
  <div class="abs years"><span class="num">35</span> YEARS</div>
  <div class="abs experience"><span class="small">OF</span><br>EXPERIENCE</div>
  <div class="abs goldbar">WORKING WITH PEOPLE THAT HAVE</div>

  <div class="abs cond" style="left:37px;top:1227px">
    <svg width="62" height="62" viewBox="0 0 62 62"><circle cx="31" cy="31" r="29" fill="none" stroke="#fff" stroke-width="1.5" stroke-dasharray="3 4"/><circle cx="33" cy="31" r="25" fill="#dba90a"/><path d="M26 44v-6c-4-2-6-6-6-10 0-7 5-11 12-11s11 5 11 10l3 6h-3v5h-6v6z" fill="#03226b"/></svg>
    Psychosocial
  </div>
  <div class="abs cond" style="left:352px;top:1227px">
    <svg width="62" height="62" viewBox="0 0 62 62"><circle cx="31" cy="31" r="29" fill="none" stroke="#fff" stroke-width="1.5" stroke-dasharray="3 4"/><circle cx="33" cy="31" r="25" fill="#dba90a"/><circle cx="33" cy="28" r="8" fill="#03226b"/><rect x="29" y="36" width="8" height="7" fill="#03226b"/></svg>
    Intellectual
  </div>
  <div class="abs cond" style="left:37px;top:1315px">
    <svg width="62" height="62" viewBox="0 0 62 62"><circle cx="31" cy="31" r="29" fill="none" stroke="#fff" stroke-width="1.5" stroke-dasharray="3 4"/><circle cx="33" cy="31" r="25" fill="#dba90a"/><path d="M26 44v-6c-4-2-6-6-6-10 0-7 5-11 12-11s11 5 11 10l3 6h-3v5h-6v6z" fill="#03226b"/></svg>
    Cognitive disabilities
  </div>

  <div class="abs aim-title">OUR <b>AIM</b></div>
  <div class="abs aim-text">Our aim to provide holistic and empowering supports targeted towards creating independence and guidance for all participants and families.</div>

  <div class="abs exp-title">EXPERIENCE IN WORKING WITH<br><span class="hl">MAINSTREAM SUPPORTS UNDER</span></div>

  <div class="abs vdash"></div>
  <div class="abs hdash" style="left:607px;top:1002px"></div>
  <div class="abs hdash" style="left:887px;top:1002px"></div>
  <div class="abs hdash" style="left:607px;top:1131px"></div>
  <div class="abs hdash" style="left:887px;top:1131px"></div>
  <div class="abs hdash" style="left:607px;top:1275px"></div>
  <div class="abs hdash" style="left:887px;top:1275px"></div>

  <div class="abs svc" style="left:611px;top:913px">
    <svg width="52" height="54" viewBox="0 0 52 54" fill="#03226b"><path d="M26 2 3 14v4h46v-4z"/><rect x="8" y="21" width="6" height="22"/><rect x="19" y="21" width="6" height="22"/><rect x="30" y="21" width="6" height="22"/><rect x="41" y="21" width="4" height="22"/><rect x="3" y="46" width="46" height="4"/></svg>
    Justice
  </div>
  <div class="abs svc" style="left:937px;top:917px">
    <svg width="52" height="46" viewBox="0 0 52 46" fill="#03226b"><rect x="1" y="2" width="23" height="40" rx="2"/><rect x="28" y="2" width="23" height="40" rx="2"/><rect x="1" y="40" width="50" height="5"/><g stroke="#fff" stroke-width="2.5"><path d="M6 12h13M6 22h13M6 32h13M33 22h13M33 32h13"/><path d="M36 8l6 6M42 8l-6 6"/></g></svg>
    Corrections
  </div>
  <div class="abs svc" style="left:611px;top:1038px">
    <svg width="54" height="50" viewBox="0 0 54 50" fill="#03226b"><path d="M22 4h10v8h8v10h-8v8H22v-8h-8V12h8z"/><path d="M2 20l6-2 8 16 8 6v8H12L2 32zM52 20l-6-2-8 16-8 6v8h12l10-16z"/></svg>
    Ulmera Health
  </div>
  <div class="abs svc" style="left:940px;top:1038px">
    <svg width="50" height="50" viewBox="0 0 50 50" fill="#03226b"><path d="M25 3 2 24h7v24h32V24h7zM7 3h5v8l-5 5z"/><path d="M19 33a7 7 0 0 1 12-4" stroke="#fff" stroke-width="2.5" fill="none"/></svg>
    Housing
  </div>
  <div class="abs svc" style="left:611px;top:1170px">
    <svg width="56" height="54" viewBox="0 0 56 54" fill="#03226b"><rect x="18" y="4" width="14" height="28" rx="3" transform="rotate(-40 25 18)"/><rect x="28" y="28" width="6" height="24" transform="rotate(-40 31 40)"/><rect x="4" y="44" width="28" height="7" rx="2"/></svg>
    Court processes
  </div>
  <div class="abs svc" style="left:948px;top:1170px">
    <svg width="50" height="52" viewBox="0 0 50 52" fill="#03226b"><rect x="4" y="12" width="32" height="36"/><rect x="22" y="6" width="10" height="24" rx="3" transform="rotate(40 27 18)" /><circle cx="40" cy="8" r="6"/><text x="8" y="44" font-family="Roboto,sans-serif" font-size="10" font-weight="700" fill="#fff">HELP</text></svg>
    Lawbridge
  </div>
  <div class="abs svc" style="left:611px;top:1313px">
    <svg width="56" height="56" viewBox="0 0 56 56" fill="#03226b"><circle cx="28" cy="8" r="6"/><path d="M18 18h20l-2 14H20z"/><path d="M2 36l8-4 8 10h26l8-6 3 4-10 10H14L4 52z"/></svg>
    Keystep Hub
  </div>
  <div class="abs svc" style="left:950px;top:1313px">
    <svg width="48" height="48" viewBox="0 0 48 48"><circle cx="24" cy="24" r="23" fill="#03226b"/><g stroke="#fff" stroke-width="3" fill="none"><path d="M12 12l8 8M20 13v7h-7M36 12l-8 8M28 13v7h7M12 36l8-8M20 35v-7h-7M36 36l-8-8M28 35v-7h7"/></g></svg>
    Paywarden
  </div>

  <div class="abs footer-gold"></div>
  <div class="abs footer-sky"></div>
  <div class="abs phone">
    <svg width="44" height="44" viewBox="0 0 24 24" fill="#03226b"><path d="M6.6 10.8a15 15 0 0 0 6.6 6.6l2.2-2.2c.3-.3.7-.4 1-.2 1.1.4 2.3.6 3.6.6.6 0 1 .4 1 1V20c0 .6-.4 1-1 1A17 17 0 0 1 3 4c0-.6.4-1 1-1h3.5c.6 0 1 .4 1 1 0 1.3.2 2.5.6 3.6.1.3 0 .7-.2 1z"/></svg>
    1800 372 519
  </div>
  <div class="abs contact" style="left:521px;top:1451px">
    <svg width="32" height="32" viewBox="0 0 32 32" fill="none" stroke="#03226b" stroke-width="2"><circle cx="16" cy="16" r="14"/><ellipse cx="16" cy="16" rx="6" ry="14"/><path d="M2 16h28M5 9h22M5 23h22"/></svg>
    www.marlowdisability.com.au
  </div>
  <div class="abs contact" style="left:836px;top:1455px">
    <svg width="30" height="22" viewBox="0 0 30 22" fill="none" stroke="#03226b" stroke-width="2"><rect x="1" y="1" width="28" height="20"/><path d="M1 1l14 11L29 1M1 21l10-9M29 21l-10-9"/></svg>
    hello@marlowdisability.com.au
  </div>

</div>
</body>
</html>
```